Consulting company needs Business Cards - rough concept provided

I'm looking for someone to take our business card idea and make is slick and polished - to communicate our high-end, sophisticated, serious consulting business. We have a rough layout we did in-house. We are open to ideas on repo-ing elements, adjusting sizes, typefaces etc... within the general concept we've already come up with. We want it to be super-clean and sophisticated. We want to keep the white backgrounds, and blue brand colors. Our goal is to print with painted blue edges on thick cardstock. Thank you!!

```html
<!DOCTYPE html>
<html lang="en">
<head>
<meta charset="utf-8">
<title>Business Cards – Front and Back</title>
<link rel="stylesheet" href="https://fonts.googleapis.com/css2?family=Work+Sans:wght@300;400;700;800&display=swap">
<style>
  :root {
    --backdrop: #9c9c9c;
    --card-white: #fbfbfb;
    --brand-blue: #1f97d8;
    --deep-blue: #1571ad;
    --edge-blue: #1763b3;
    --ink: #1d1d1d;
    --muted: #b4b4b4;
  }
  * { margin: 0; padding: 0; box-sizing: border-box; }
  html, body {
    width: 1200px;
    height: 1000px;
    overflow: hidden;
    background: var(--backdrop);
    font-family: "Work Sans", sans-serif;
  }
  .card {
    position: absolute;
    width: 700px;
    height: 400px;
    background: var(--card-white);
    border-bottom: 6px solid var(--edge-blue);
    border-left: 3px solid var(--edge-blue);
    overflow: hidden;
  }
  .card--front { left: 110px; top: 70px; }
  .card--back { left: 400px; top: 530px; }

  .brand {
    position: absolute;
    right: 40px;
    top: 40px;
    display: flex;
    align-items: center;
    gap: 14px;
  }
  .brand__mark {
    width: 28px;
    height: 28px;
    background: var(--brand-blue);
  }
  .brand__name {
    font-weight: 700;
    font-size: 34px;
    line-height: 1;
    color: var(--ink);
  }
  .identity {
    position: absolute;
    left: 60px;
    top: 190px;
  }
  .identity__name {
    font-weight: 800;
    font-size: 26px;
    color: var(--ink);
  }
  .identity__role {
    font-weight: 300;
    font-size: 19px;
    color: var(--ink);
    margin-top: 2px;
    padding-left: 30px;
  }
  .contact {
    position: absolute;
    left: 380px;
    top: 230px;
    font-weight: 300;
    font-size: 19px;
    line-height: 1.3;
    color: var(--ink);
    list-style: none;
  }

  .positioning {
    position: absolute;
    left: 40px;
    top: 34px;
    font-size: 45px;
    line-height: 1.18;
    font-weight: 300;
    color: var(--muted);
  }
  .positioning .lead { font-weight: 800; color: var(--deep-blue); }
  .positioning .key { font-weight: 800; color: var(--brand-blue); }
</style>
</head>
<body>
  <section class="card card--front" aria-label="Card front">
    <div class="brand">
      <span class="brand__mark"></span>
      <span class="brand__name">Tinymammoth</span>
    </div>
    <div class="identity">
      <p class="identity__name">Dana Whitfield</p>
      <p class="identity__role">Brand Consultant</p>
    </div>
    <ul class="contact">
      <li>4820 Harbor Lane, Ste 210</li>
      <li>Lakeview, CA 90210</li>
      <li>(555) 014 2290</li>
      <li>dana@tinymammoth.com</li>
      <li>tinymammoth.com</li>
    </ul>
  </section>

  <section class="card card--back" aria-label="Card back">
    <p class="positioning">
      <span class="lead">We help</span> [target audience]<br>
      <span class="key">achieve</span> [desired emotional<br>
      outcome] <span class="key">by</span> [our unique<br>
      approach] <span class="key">because</span> [our<br>
      brand beliefs].
    </p>
  </section>
</body>
</html>
```